Business Card Design Project

I have a need for a business card designed. I have a logo.. but need looking for a nice card to go with it. The school is called The Bramblecrest Movement School is the name of the school. Some ideas for what I want on the card.
Guru Reid Pashley
over 25 years martial arts experience
Private and group lessons
kids and adult classes
No contracts or testing fees
styles we teach are escrima, silat, kenpo, and MMA
website is www.bramblecrestms.net
phone is 914-555-0173
visit us on pal net at https://www.palnet.example/pages/The-Bramblecrest-Movement-School/482930175620394

Target Market(s)

adults 1st kids second.

Industry/Entity Type

School

Requirements
Must have
• Guru Reid Pashley
Private and group lessons
phone is 914-555-0173

```html
<!DOCTYPE html>
<html lang="en">
<head>
<meta charset="utf-8">
<title>The Bramblecrest Movement School – Business Cards</title>
<link rel="stylesheet" href="https://fonts.googleapis.com/css2?family=Fira+Sans:ital,wght@0,400;0,700;0,800;1,400;1,600&display=swap">
<style>
  :root {
    --bg-light: #ffffff;
    --bg-sky: #bfe3fb;
    --yellow: #fff200;
    --band-yellow: #f7ee1c;
    --red-hot: #c8211b;
    --red-deep: #8c0a0a;
    --red-band: #b3140f;
    --navy: #0d3a78;
    --navy-band: #0b3466;
    --charcoal: #2a2727;
    --charcoal-band: #231f20;
    --frame-black: #1b1b1b;
    --ink: #1d1d1b;
    --white: #ffffff;
  }
  * { box-sizing: border-box; margin: 0; padding: 0; }
  html, body { width: 1200px; height: 1000px; overflow: hidden; }
  body {
    position: relative;
    font-family: "Fira Sans", Arial, sans-serif;
    background: radial-gradient(ellipse at 62% 45%, var(--bg-light) 0%, #e6f4fd 40%, var(--bg-sky) 100%);
  }

  .card { position: absolute; }
  .face { position: absolute; overflow: hidden; }

  /* school name set where the mark stands */
  .school-mark {
    position: absolute; left: 0; right: 0;
    display: flex; align-items: center; justify-content: center;
    text-align: center;
    color: var(--yellow);
    font-weight: 800;
    text-transform: uppercase;
    line-height: 1.05;
  }

  /* front card sections */
  .styles-taught {
    position: absolute; left: 0; right: 0; top: 220px; height: 64px;
    display: block;
    padding-top: 4px;
    color: var(--white); font-weight: 700; font-size: 25px; line-height: 28px;
    text-align: center; text-shadow: 1px 1px 2px rgba(0,0,0,.6);
    letter-spacing: .3px;
    white-space: nowrap;
  }
  .styles-taught .and { font-size: 19px; }
  .band { position: absolute; left: 0; right: 0; text-align: center; }
  .band-instructor {
    top: 290px; height: 48px; background: var(--band-yellow); color: var(--ink);
    padding-top: 5px;
  }
  .band-instructor .name { font-weight: 700; font-size: 19px; line-height: 22px; }
  .band-instructor .experience { font-style: italic; font-size: 11.5px; font-weight: 600; }
  .band-lessons {
    top: 344px; height: 52px; color: var(--white); font-size: 14px; line-height: 18px;
    padding-top: 8px;
  }
  .band-contact {
    top: 400px; height: 44px; color: var(--white); padding-top: 3px;
  }
  .band-contact .phone { font-weight: 700; font-size: 21px; line-height: 23px; letter-spacing: .3px; }
  .band-contact .web { font-weight: 700; font-size: 12.5px; letter-spacing: .6px; }

  /* red front */
  .card-red-front { left: 157px; top: 92px; width: 268px; height: 468px; background: var(--yellow); }
  .card-red-front .face {
    left: 11px; top: 11px; width: 246px; height: 446px;
    background:
      radial-gradient(circle 150px at 50% 20%, #f07a18 0%, rgba(200,33,27,0) 100%),
      linear-gradient(180deg, var(--red-hot) 0%, var(--red-deep) 70%);
    box-shadow: 4px 5px 4px rgba(0,0,0,.65);
  }
  .card-red-front .band-lessons { background: var(--red-band); }
  .card-red-front .band-contact { background: var(--navy-band); }

  /* black front */
  .card-black-front { left: 908px; top: 12px; width: 270px; height: 470px; background: var(--frame-black); }
  .card-black-front .face {
    left: 12px; top: 12px; width: 246px; height: 446px;
    background: radial-gradient(circle 140px at 50% 28%, #e9e21a 0%, #6d6a1c 55%, var(--charcoal) 100%);
  }
  .card-black-front .band-lessons { background: var(--charcoal-band); }
  .card-black-front .band-contact { background: var(--red-band); }

  /* blue front */
  .card-blue-front { left: 626px; top: 515px; width: 269px; height: 472px; background: var(--frame-black); }
  .card-blue-front .face {
    left: 11px; top: 11px; width: 247px; height: 450px; background: var(--navy);
  }
  .card-blue-front .band-lessons { background: var(--navy-band); }
  .card-blue-front .band-contact { background: var(--red-band); }

  .front .school-mark { top: 40px; height: 150px; font-size: 26px; padding: 0 18px; }

  /* backs */
  .back .inner-rule {
    position: absolute; inset: 10px; border: 1.5px solid var(--yellow);
  }
  .back .school-mark { top: 0; bottom: 0; font-size: 18px; padding: 0 40px; }

  .card-black-back { left: 626px; top: 12px; width: 269px; height: 470px; background: var(--frame-black); }
  .card-black-back .face { inset: 0; background: var(--charcoal); border: 2px solid var(--frame-black); }

  .card-blue-back { left: 908px; top: 515px; width: 270px; height: 470px; background: var(--frame-black); }
  .card-blue-back .face { inset: 0; background: var(--navy); border: 2px solid var(--frame-black); }

  .card-red-back { left: 57px; top: 577px; width: 468px; height: 268px; background: var(--yellow); }
  .card-red-back .face {
    left: 11px; top: 11px; width: 446px; height: 246px;
    background: linear-gradient(180deg, #b5151a 0%, var(--red-deep) 100%);
  }
  .card-red-back .school-mark { font-size: 22px; padding: 0 110px; }
</style>
</head>
<body>

  <!-- red card, front -->
  <section class="card card-red-front front">
    <div class="face">
      <div class="school-mark">The Bramblecrest Movement School</div>
      <h2 class="styles-taught">ESCRIMA, SILAT,<br>KENPO <span class="and">AND</span> MMA</h2>
      <div class="band band-instructor">
        <div class="name">Guru Reid Pashley</div>
        <div class="experience">over 25 years martial arts experience</div>
      </div>
      <div class="band band-lessons">• Private and group lessons<br>• No contracts or testing fees</div>
      <div class="band band-contact">
        <div class="phone">914-555-0173</div>
        <div class="web">www.bramblecrestms.net</div>
      </div>
    </div>
  </section>

  <!-- red card, back -->
  <section class="card card-red-back back">
    <div class="face">
      <div class="school-mark">The Bramblecrest Movement School</div>
    </div>
  </section>

  <!-- black card, back -->
  <section class="card card-black-back back">
    <div class="face">
      <div class="inner-rule"></div>
      <div class="school-mark">The Bramblecrest Movement School</div>
    </div>
  </section>

  <!-- black card, front -->
  <section class="card card-black-front front">
    <div class="face">
      <div class="school-mark">The Bramblecrest Movement School</div>
      <h2 class="styles-taught">ESCRIMA, SILAT,<br>KENPO <span class="and">AND</span> MMA</h2>
      <div class="band band-instructor">
        <div class="name">Guru Reid Pashley</div>
        <div class="experience">over 25 years martial arts experience</div>
      </div>
      <div class="band band-lessons">• Private and group lessons<br>• No contracts or testing fees</div>
      <div class="band band-contact">
        <div class="phone">914-555-0173</div>
        <div class="web">www.bramblecrestms.net</div>
      </div>
    </div>
  </section>

  <!-- blue card, front -->
  <section class="card card-blue-front front">
    <div class="face">
      <div class="school-mark">The Bramblecrest Movement School</div>
      <h2 class="styles-taught">ESCRIMA, SILAT,<br>KENPO <span class="and">AND</span> MMA</h2>
      <div class="band band-instructor">
        <div class="name">Guru Reid Pashley</div>
        <div class="experience">over 25 years martial arts experience</div>
      </div>
      <div class="band band-lessons">• Private and group lessons<br>• No contracts or testing fees</div>
      <div class="band band-contact">
        <div class="phone">914-555-0173</div>
        <div class="web">www.bramblecrestms.net</div>
      </div>
    </div>
  </section>

  <!-- blue card, back -->
  <section class="card card-blue-back back">
    <div class="face">
      <div class="inner-rule"></div>
      <div class="school-mark">The Bramblecrest Movement School</div>
    </div>
  </section>

</body>
</html>
```